New iOS App design for Boston Startup

We are looking for a new app design for our Zorvak app. The current app's design feels outdated and we like to add lots of new functionality and a new navigation as well. A complete overhaul therefore!
We want you to design 5 screens that will have changed the most. The complete wireframes of these 5 pages are attached in the requirements document.
Once the winning design is selected we will award the winner with the designing all other screens (40-50 screens based on the same design). This will be a separate project worth $1000. The winning designer can get more follow up work if both sides are happy about the cooperation.
We will give feedback as soon as the first screen has been uploaded for review. Final decision will be made only after all 5 screens are finished.
We hope you give it your best!
Note: will only communicate through PixelGuild (no skype),
Updates
Project Deadline Extended
Reason: Want to give designers a chance to submit their designs as I understand from some, the deadline is too close.
I have raised the award and introduced a 2nd price as well to make it worth your time. I hope you give it your best shot.
Project Deadline Extended
Reason: A few of you have asked for an extension of the deadline as time is running out. I will extend by one day. Tell me if you need more.
Industry/Entity Type
Startup
Requirements
Must have
- At least 1 screen before we can give you feedback.
Nice to have
- multiple options of 1 screen to get to a desirable design

```html
<!DOCTYPE html>
<html lang="en">
<head>
<meta charset="utf-8">
<title>Zorvak – Study App Screens</title>
<link rel="stylesheet" href="https://fonts.googleapis.com/css2?family=Roboto:wght@300;400;500;700&display=swap">
<style>
:root{
  --stage:#1d1d1d;
  --red:#ef5350;
  --red-dark:#d9403d;
  --green:#3fba4f;
  --blue:#3a9de3;
  --orange:#f6b42b;
  --yellow:#f3c340;
  --ink:#333;
  --muted:#777;
  --line:#d8d8d8;
  --panel:#2d3a47;
  --panel-line:#3e4c5a;
  --white:#fff;
  --black:#000;
}
*{box-sizing:border-box;margin:0;padding:0}
html,body{width:1200px;height:657px;overflow:hidden;background:var(--stage);font-family:"Roboto",Arial,sans-serif;color:var(--ink)}
.stage{position:relative;width:1200px;height:657px}
.screen{position:absolute;width:207px;height:360px;background:var(--white);overflow:hidden;transform-origin:0 0}
.screen--timeline{left:40px;top:198px;transform:scale(.787)}
.screen--practice{left:252px;top:178px;transform:scale(.884)}
.screen--home{left:497px;top:158px}
.screen--menu{left:767px;top:178px;transform:scale(.884)}
.screen--analytics{left:1000px;top:198px;transform:scale(.787)}

.status-bar{position:absolute;left:0;top:0;width:100%;height:11px;background:var(--black);color:var(--white);font-size:6px;font-weight:500;display:flex;align-items:center;justify-content:space-between;padding:0 5px}
.status-bar .time{position:absolute;left:0;right:0;text-align:center}
.status-bar .battery{width:10px;height:5px;border:1px solid var(--white);border-radius:1px;position:relative}
.status-bar .battery::after{content:"";position:absolute;inset:1px;background:var(--white)}

.app-header{position:absolute;left:0;top:11px;width:100%;height:22px;background:var(--red);color:var(--white);font-size:10px;font-weight:300;display:flex;align-items:center;justify-content:center}
.app-header .back{position:absolute;left:5px;top:5px;width:12px;height:12px;border-radius:50%;background:var(--white)}
.app-header .hamburger{position:absolute;left:6px;top:6px;width:12px;height:10px}

.tab-bar{position:absolute;left:0;bottom:0;width:100%;height:42px;border-top:1px solid var(--line);background:#fafafa;display:flex}
.tab{flex:1;display:flex;flex-direction:column;align-items:center;justify-content:center;font-size:5.5px;color:var(--muted);gap:3px}
.tab svg{width:15px;height:13px}
.tab--active{background:var(--red);color:var(--white);margin:4px 5px}

/* Timeline */
.test-date{position:absolute;left:8px;top:50px;font-size:7px}
.change-btn{position:absolute;right:8px;top:47px;background:var(--orange);border-radius:6px;font-size:7px;padding:2px 9px;box-shadow:0 1px 0 #b77d10}
.completion-label{position:absolute;left:0;right:0;top:76px;text-align:center;font-size:7px}
.completion-track{position:absolute;left:8px;right:8px;top:88px;height:4px;background:#e6e6e6}
.completion-track span{display:block;width:48%;height:100%;background:var(--green)}
.completion-scale{position:absolute;left:8px;right:8px;top:96px;display:flex;justify-content:space-between;font-size:7px}
.timeline-chart{position:absolute;left:6px;top:120px;width:196px;height:160px}

/* Practice */
.lesson{position:absolute;left:7px;width:194px;height:28px;border-radius:7px;color:var(--white);font-size:7px;display:flex;align-items:center;padding:0 10px;box-shadow:0 2px 0 rgba(0,0,0,.15)}
.lesson::before{content:"";position:absolute;left:6px;bottom:-5px;border-left:6px solid transparent;border-right:6px solid transparent;border-top:6px solid currentColor;color:inherit}
.lesson--one{top:53px;background:var(--yellow)}
.lesson--one::before{border-top-color:var(--yellow)}
.lesson--two{top:93px;background:var(--green)}
.lesson--two::before{border-top-color:var(--green)}
.lesson--three{top:130px;background:var(--blue)}
.lesson--three::before{border-top-color:var(--blue)}
.lesson svg{position:absolute;right:26px;top:7px;width:14px;height:14px}
.lesson .chev{position:absolute;right:8px;top:7px;font-size:11px;line-height:14px}

/* Home */
.profile{position:absolute;left:0;top:33px;width:100%;height:96px;background:linear-gradient(160deg,#8fa2b4,#5b7186 55%,#8496a8)}
.avatar{position:absolute;left:6px;top:14px;width:56px;height:56px;border-radius:50%;border:2px solid var(--white);background:linear-gradient(#d9c3b0,#a98e7c)}
.profile-name{position:absolute;left:72px;top:17px;color:var(--white);font-size:13px;font-weight:700}
.profile-place{position:absolute;left:72px;top:34px;color:var(--white);font-size:6.5px;display:flex;gap:2px;align-items:center}
.score{color:var(--white);font-size:11px;font-weight:300;display:flex;align-items:baseline;gap:3px}
.score strong{font-size:17px;font-weight:400}
.score .delta{font-size:7px}
.profile .score{position:absolute;left:72px;top:48px}
.arrow-down{color:var(--red);font-weight:700}
.stats{position:absolute;left:0;width:100%;height:30px;background:#f3f3f3;display:flex;border-bottom:2px solid var(--red)}
.stat{flex:1;border-right:1px solid var(--line);display:flex;flex-direction:column;justify-content:center;padding-left:4px;font-size:9px}
.stat small{font-size:6.5px;color:var(--muted)}
.stat .up{color:var(--green);font-weight:700}
.stat--week{flex:.9;font-size:6.5px;color:var(--muted);justify-content:flex-end;padding-bottom:4px}
.screen--home .stats{top:129px}
.action{position:absolute;top:175px;width:58px;height:58px;border-radius:50%;color:var(--white);font-size:8px;text-align:center;display:flex;flex-direction:column;align-items:center;justify-content:center;box-shadow:0 2px 0 rgba(0,0,0,.2)}
.action--analytics{left:6px;background:var(--green)}
.action--course{left:74px;background:var(--blue)}
.action--days{left:142px;background:var(--orange)}
.divider{position:absolute;left:0;right:0;top:248px;height:1px;background:var(--line)}
.up-next{position:absolute;left:68px;top:260px;width:134px;height:42px;background:var(--red);border-radius:8px;color:var(--white);text-align:center;font-size:7px;padding-top:9px}
.up-next strong{display:block;font-size:10px;font-weight:400;margin-top:2px}
.up-next::after{content:"";position:absolute;right:-2px;bottom:-5px;border-left:8px solid var(--red);border-bottom:6px solid transparent}

/* Menu */
.menu-panel{position:absolute;left:0;top:11px;width:178px;bottom:0;background:var(--panel)}
.menu-title{height:23px;background:#d6dbe0;color:var(--ink);font-size:9px;display:flex;align-items:center;justify-content:center}
.menu-item{position:absolute;left:0;width:100%;height:36px;border-bottom:1px solid var(--panel-line);color:var(--white);font-size:8px;display:flex;align-items:center;padding-left:26px}
.menu-item i{position:absolute;left:8px;width:8px;height:8px;background:var(--red);border-radius:2px}
.menu-item .badge{position:absolute;right:8px;font-size:6px;padding:1px 3px;border-radius:1px;font-style:normal}
.badge--green{background:var(--green)}
.badge--blue{background:var(--blue)}
.peek{position:absolute;left:178px;top:11px;width:29px;bottom:0;background:var(--white);border-left:1px solid #000}
.peek-header{height:22px;background:var(--red)}
.peek-photo{height:96px;background:linear-gradient(160deg,#8fa2b4,#5b7186)}
.peek-stats{height:30px;background:#f3f3f3;border-bottom:2px solid var(--red);font-size:8px;padding:6px 0 0 3px}
.peek-circle{position:absolute;left:4px;top:164px;width:58px;height:58px;border-radius:50%;background:var(--green)}

/* Analytics */
.banner{position:absolute;left:0;top:33px;width:100%;height:80px;background:linear-gradient(170deg,#9cafbd,#5f7484 60%,#3d4d59);display:flex;justify-content:center;align-items:center}
.screen--analytics .stats{top:113px}
.subject{position:absolute;left:6px;right:8px;height:14px;display:flex;align-items:center;font-size:5.5px;font-weight:500}
.subject .track{position:absolute;left:79px;right:0;height:14px;border:1px solid #bbb;background:#eee;border-radius:2px;overflow:hidden}
.subject .fill{height:100%;color:var(--ink);font-size:6px;padding-left:3px;display:flex;align-items:center}
.fill--green{background:var(--green)}
.fill--blue{background:var(--blue)}
.fill--orange{background:var(--orange)}
</style>
</head>
<body>
<main class="stage">

<svg width="0" height="0" style="position:absolute" aria-hidden="true">
  <defs>
    <g id="icon-theory"><rect x="1" y="2" width="13" height="2" fill="#555"/><rect x="2" y="6" width="11" height="2" fill="#555"/><rect x="1" y="10" width="13" height="2" fill="#555"/></g>
    <g id="icon-practice"><rect x="3" y="1" width="9" height="12" rx="1" fill="none" stroke="currentColor" stroke-width="1.3"/><rect x="5" y="0" width="5" height="2" fill="currentColor"/><path d="M5 5h5M5 8h5" stroke="currentColor"/></g>
    <g id="icon-home"><path d="M7.5 1L1 7h2v6h3.5V9h2v4H12V7h2z" fill="currentColor"/></g>
    <g id="icon-games"><path d="M3 4h9a3 3 0 0 1 2 5l-1 2-3-2H5l-3 2-1-2a3 3 0 0 1 2-5z" fill="currentColor"/></g>
    <g id="icon-test"><rect x="3" y="1" width="9" height="12" fill="none" stroke="currentColor" stroke-width="1.2"/><path d="M5 4h5M5 7h5M5 10h3" stroke="currentColor"/></g>
  </defs>
</svg>

<!-- Timeline screen -->
<section class="screen screen--timeline">
  <div class="status-bar"><span>.ıll NOVA 3G</span><span class="time">9:51 PM</span><span class="battery"></span></div>
  <header class="app-header"><span class="back"></span>Timeline</header>
  <p class="test-date">Your Test date: 4 Nov 2013</p>
  <span class="change-btn">change</span>
  <p class="completion-label">Completion :</p>
  <div class="completion-track"><span></span></div>
  <div class="completion-scale"><span>0%</span><span>48%</span><span>100%</span></div>
  <svg class="timeline-chart" viewBox="0 0 196 160">
    <text x="10" y="10" font-size="6.5" fill="#333">100%</text>
    <text x="16" y="136" font-size="6.5" fill="#333">0%</text>
    <text transform="translate(12 95) rotate(-90)" font-size="6.5" fill="#333">Completion</text>
    <rect x="28" y="6" width="164" height="128" fill="#f6b42b"/>
    <polygon points="28,134 192,6 192,134" fill="#3a9de3"/>
    <polyline points="28,130 72,112 120,90 148,50 192,6" fill="none" stroke="#1f4f8a" stroke-width="2.5"/>
    <circle cx="72" cy="112" r="4" fill="#3fba4f" stroke="#fff"/>
    <circle cx="120" cy="90" r="4" fill="#3fba4f" stroke="#fff"/>
    <circle cx="148" cy="50" r="5" fill="#1f4f8a" stroke="#ef5350" stroke-width="2"/>
    <text x="50" y="22" font-size="7" fill="#333">Ahead of schedule</text>
    <text x="130" y="122" font-size="7" fill="#fff">Behind schedule</text>
    <text x="22" y="148" font-size="6.5" fill="#333">1 Sep 13</text>
    <text x="98" y="148" font-size="6.5" fill="#333">time</text>
    <text x="164" y="148" font-size="6.5" fill="#333">4 Nov 13</text>
  </svg>
  <nav class="tab-bar">
    <span class="tab"><svg viewBox="0 0 15 13"><use href="#icon-theory"/></svg>Theory</span>
    <span class="tab"><svg viewBox="0 0 15 13"><use href="#icon-practice"/></svg>Practice</span>
    <span class="tab"><svg viewBox="0 0 15 13"><use href="#icon-home"/></svg>Home</span>
    <span class="tab"><svg viewBox="0 0 15 13"><use href="#icon-games"/></svg>Games</span>
    <span class="tab"><svg viewBox="0 0 15 13"><use href="#icon-test"/></svg>Test</span>
  </nav>
</section>

<!-- Practice screen -->
<section class="screen screen--practice">
  <div class="status-bar"><span>.ıll NOVA 3G</span><span class="time">9:51 PM</span><span class="battery"></span></div>
  <header class="app-header"><span class="back"></span>Practice - SC</header>
  <div class="lesson lesson--one">Lesson 1: Sentence Correction
    <svg viewBox="0 0 14 14"><path d="M3 13V6l4-5 1 1-1 4h5l-1 7z" fill="#fff"/></svg><span class="chev">›</span></div>
  <div class="lesson lesson--two">Lesson 2 : Sentence Correction
    <svg viewBox="0 0 14 14"><path d="M3 13V6l4-5 1 1-1 4h5l-1 7z" fill="#fff"/></svg><span class="chev">›</span></div>
  <div class="lesson lesson--three">Lesson 3: Sentence Correction
    <svg viewBox="0 0 14 14"><circle cx="7" cy="7" r="6.5" fill="#fff"/><path d="M4 7a3 3 0 0 1 5-2M10 7a3 3 0 0 1-5 2" stroke="#3a9de3" stroke-width="1.4" fill="none"/></svg><span class="chev">›</span></div>
  <nav class="tab-bar">
    <span class="tab"><svg viewBox="0 0 15 13"><use href="#icon-theory"/></svg>Theory</span>
    <span class="tab tab--active"><svg viewBox="0 0 15 13"><use href="#icon-practice"/></svg>Practice</span>
    <span class="tab"><svg viewBox="0 0 15 13"><use href="#icon-home"/></svg>Home</span>
    <span class="tab"><svg viewBox="0 0 15 13"><use href="#icon-games"/></svg>Games</span>
    <span class="tab"><svg viewBox="0 0 15 13"><use href="#icon-test"/></svg>Test</span>
  </nav>
</section>

<!-- Home screen -->
<section class="screen screen--home">
  <div class="status-bar"><span>.ıll NOVA 3G</span><span class="time">9:51 PM</span><span class="battery"></span></div>
  <header class="app-header">
    <svg class="hamburger" viewBox="0 0 12 10"><path d="M0 1h12M0 5h12M0 9h12" stroke="#fff" stroke-width="1.6"/></svg>
    Welcome back, Rafi</header>
  <div class="profile" role="img" aria-label="Blurred architectural photo backdrop">
    <div class="avatar" role="img" aria-label="User profile photo"></div>
    <p class="profile-name">Rafi Moran</p>
    <p class="profile-place"><svg width="5" height="7" viewBox="0 0 5 7"><path d="M2.5 7L0 3a2.5 2.5 0 1 1 5 0z" fill="#fff"/></svg>Bayview, CA</p>
    <p class="score">Score <strong>650</strong><span class="arrow-down">↓</span><span class="delta">-18</span></p>
  </div>
  <div class="stats">
    <div class="stat"><span>34%<span class="up">↑</span>+4</span><small>Completion</small></div>
    <div class="stat"><span>20<span class="up">↑</span>+3</span><small>Sessions</small></div>
    <div class="stat"><span>18<span class="up">↑</span>+10</span><small>Min.</small></div>
    <div class="stat stat--week">This week</div>
  </div>
  <div class="action action--analytics">Analytics<span>^</span></div>
  <div class="action action--course">Course<br>Overview<span>^</span></div>
  <div class="action action--days">Days until<br>test 33<span>^</span></div>
  <div class="divider"></div>
  <div class="up-next">Up Next: Sentence Correction<strong>Lesson 4</strong></div>
  <nav class="tab-bar">
    <span class="tab"><svg viewBox="0 0 15 13"><use href="#icon-theory"/></svg>Theory</span>
    <span class="tab"><svg viewBox="0 0 15 13"><use href="#icon-practice"/></svg>Practice</span>
    <span class="tab tab--active"><svg viewBox="0 0 15 13"><use href="#icon-home"/></svg>Home</span>
    <span class="tab"><svg viewBox="0 0 15 13"><use href="#icon-games"/></svg>Games</span>
    <span class="tab"><svg viewBox="0 0 15 13"><use href="#icon-test"/></svg>Test</span>
  </nav>
</section>

<!-- Menu screen -->
<section class="screen screen--menu">
  <div class="status-bar"><span>.ıll NOVA 3G</span><span class="time">9:51 PM</span><span class="battery"></span></div>
  <div class="peek">
    <div class="peek-header"></div>
    <div class="peek-photo" role="img" aria-label="Blurred architectural photo backdrop"></div>
    <div class="peek-stats">29%</div>
    <div class="peek-circle"></div>
  </div>
  <nav class="menu-panel">
    <div class="menu-title">Menu</div>
    <div class="menu-item" style="top:34px"><i></i>Profile</div>
    <div class="menu-item" style="top:70px"><i></i>My Tutor<em class="badge badge--green">8</em></div>
    <div class="menu-item" style="top:106px"><i></i>Advanced Writing Assignment<br>(AWA)</div>
    <div class="menu-item" style="top:142px"><i></i>Social<em class="badge badge--blue">6</em></div>
    <div class="menu-item" style="top:178px"><i></i>Vocabulary</div>
    <div class="menu-item" style="top:214px"><i></i>Marketplace</div>
    <div class="menu-item" style="top:250px"><i></i>Settings</div>
    <div class="menu-item" style="top:286px"><i></i>About the GRADX</div>
  </nav>
</section>

<!-- Analytics screen -->
<section class="screen screen--analytics">
  <div class="status-bar"><span>.ıll NOVA 3G</span><span class="time">9:51 PM</span><span class="battery"></span></div>
  <header class="app-header"><span class="back"></span>Analytics</header>
  <div class="banner" role="img" aria-label="Blurred seaside rocks photo backdrop">
    <p class="score">Score <strong>650</strong><span class="arrow-down">↓</span><span class="delta">-18</span></p>
  </div>
  <div class="stats">
    <div class="stat"><span>34%<span class="up">↑</span>+4</span><small>Completion</small></div>
    <div class="stat"><span>20<span class="up">↑</span>+3</span><small>Sessions</small></div>
    <div class="stat"><span>18<span class="up">↑</span>+10</span><small>Min.</small></div>
    <div class="stat stat--week">This week</div>
  </div>
  <div class="subject" style="top:172px">Sentence Correction<span class="track"><span class="fill fill--green" style="width:58%">710</span></span></div>
  <div class="subject" style="top:197px">Critical Reasoning<span class="track"><span class="fill fill--blue" style="width:28%">225</span></span></div>
  <div class="subject" style="top:222px">Reading Comprehension<span class="track"><span class="fill fill--orange" style="width:43%">465</span></span></div>
  <div class="subject" style="top:249px">Data Sufficiency<span class="track"><span class="fill fill--green" style="width:58%">710</span></span></div>
  <div class="subject" style="top:275px">Problem Solving<span class="track"><span class="fill fill--blue" style="width:28%">225</span></span></div>
  <div class="subject" style="top:300px">Pace<span class="track"><span class="fill fill--orange" style="width:43%">465</span></span></div>
  <nav class="tab-bar">
    <span class="tab"><svg viewBox="0 0 15 13"><use href="#icon-theory"/></svg>Theory</span>
    <span class="tab"><svg viewBox="0 0 15 13"><use href="#icon-practice"/></svg>Practice</span>
    <span class="tab"><svg viewBox="0 0 15 13"><use href="#icon-home"/></svg>Home</span>
    <span class="tab"><svg viewBox="0 0 15 13"><use href="#icon-games"/></svg>Games</span>
    <span class="tab"><svg viewBox="0 0 15 13"><use href="#icon-test"/></svg>Test</span>
  </nav>
</section>

</main>
</body>
</html>
```